Valmin & Co Powerpoint Template

A simple powerpoint template for my business which provides management consulting services for Business Owners.

It should reflect the colours within the logo design and should work as the master template for all standard powerpoint slide layouts.

```html
<!DOCTYPE html>
<html lang="en">
<head>
<meta charset="utf-8">
<title>Valmin &amp; Co – Presentation Template</title>
<link href="https://fonts.googleapis.com/css2?family=Montserrat:wght@300;400;500;600;700&display=swap" rel="stylesheet">
<style>
:root{
  --orange:#e0561f;
  --orange-soft:#f08a4b;
  --brown:#7a2a12;
  --brown-dark:#561a08;
  --band:#ececec;
  --text:#6f6f6f;
  --ink:#333;
  --row-a:#f6dcd2;
  --row-b:#fbeee9;
}
*{box-sizing:border-box;margin:0;padding:0}
html,body{width:1200px;height:1200px;overflow:hidden;background:#fff;font-family:"Montserrat",sans-serif}
.canvas{position:relative;width:1200px;height:1200px}
.slide{position:absolute;width:427px;height:240px;background:#fff;overflow:hidden;transform:scale(.6206);transform-origin:0 0;box-shadow:0 6px 14px rgba(0,0,0,.18)}
.brand{position:absolute;top:18px;right:26px;display:flex;align-items:center;gap:3px;font-size:5px;font-weight:600;color:var(--orange)}
.brand i{display:block;width:6px;height:6px;background:var(--orange)}
.foot{position:absolute;bottom:7px;left:20px;right:20px;display:flex;justify-content:space-between;font-size:4.5px;color:#aaa}
.foot span:last-child{color:var(--orange)}
.ttl{position:absolute;top:22px;left:0;right:0;text-align:center;font-size:13px;font-weight:400;color:var(--orange)}
.rule{position:absolute;top:42px;left:0;right:0;height:1px;background:#e4e4e4}
.band{position:absolute;top:43px;left:0;right:0;padding:3px 30px;background:var(--band);font-size:4.6px;line-height:1.3;text-align:center;color:var(--text)}
.p{font-size:4.6px;line-height:1.38;color:var(--text)}
.h{font-size:5.5px;font-weight:600;color:var(--brown)}
.ho{font-size:5.5px;font-weight:600;color:var(--orange)}
.photo{position:absolute;background:linear-gradient(135deg,#c9d3de,#6f86a8 55%,#2c3d5c)}
.photo.warm{background:linear-gradient(135deg,#e6d8cc,#a48a76 50%,#3c3f52)}
.abs{position:absolute}
.num{font-size:14px;font-weight:300;color:var(--orange)}
.num.dark{color:var(--brown)}
.cols3{position:absolute;display:grid;grid-template-columns:repeat(3,1fr);gap:10px}
table.data{position:absolute;left:18px;right:18px;top:98px;border-collapse:collapse;width:391px;font-size:6px;color:var(--ink)}
table.data th{background:var(--orange);color:#fff;font-weight:600;height:16px}
table.data td{text-align:center;height:16px}
table.data tr:nth-child(odd) td{background:var(--row-a)}
table.data tr:nth-child(even) td{background:var(--row-b)}
table.data td:first-child{font-weight:700;background:#f3c9b8}
.circle{position:absolute;border-radius:50%}
</style>
</head>
<body>
<main class="canvas">

<!-- Row 1 -->
<section class="slide cover" style="left:29px;top:94px">
  <div class="photo" role="img" aria-label="Landscape photo of green mangrove trees under a bright sky" style="inset:0;background:linear-gradient(100deg,#e9ecef 0%,#cfd9d6 35%,#8fab6e 60%,#4f7a2e 85%,#9db8c7 100%)"></div>
  <div class="abs" style="left:-80px;top:-40px;width:330px;height:330px;border-radius:50%;background:rgba(255,255,255,.55)"></div>
  <div class="abs" style="left:120px;top:44px;font-size:20px;font-weight:400;color:var(--brown);line-height:1.05">Valmin<br>&amp; Co</div>
  <div class="abs" style="left:0;width:260px;top:116px;text-align:center;font-size:7px;color:#444">Supporting Business Owners</div>
  <div class="abs" style="left:0;width:260px;top:132px;text-align:center;font-size:8px;color:#333">TITLE PRESENTATION GOES HERE</div>
  <div class="abs" style="left:0;width:260px;top:148px;text-align:center;font-size:6px;color:#444">Place here your subtitle presentation here</div>
  <div class="abs" style="left:0;width:260px;top:160px;text-align:center;font-size:4.5px;color:#555">Mark Dalton / sep 1, 2023</div>
  <div class="foot"><span>Copyright © 2023 Valmin &amp; Co</span><span></span></div>
</section>

<section class="slide" style="left:323px;top:94px">
  <div class="brand"><i></i>Valmin &amp; Co</div>
  <div class="ttl" style="top:14px">Two Columns And Images</div>
  <div class="abs ho" style="left:40px;width:133px;top:40px;text-align:center;font-size:8px;font-weight:400">Your Subtitle Here</div>
  <div class="abs ho" style="left:254px;width:133px;top:40px;text-align:center;font-size:8px;font-weight:400">Your Subtitle Here</div>
  <div class="photo" role="img" aria-label="Photo of a team reviewing documents" style="left:58px;top:58px;width:133px;height:68px"></div>
  <div class="photo warm" role="img" aria-label="Photo of hands working with charts on a desk" style="left:248px;top:58px;width:133px;height:68px"></div>
  <p class="abs p" style="left:58px;width:133px;top:132px;text-align:center">Lorem Ipsum is simply dummy text of the printing and typesetting industry. Lorem Ipsum has been the industry's standard dummy text ever since the 1500s, when</p>
  <p class="abs p" style="left:248px;width:133px;top:132px;text-align:center">Lorem Ipsum is simply dummy text of the printing and typesetting industry. Lorem Ipsum has been the industry's standard dummy text ever since the 1500s, when</p>
  <div class="foot"><span>Copyright © 2023 Valmin &amp; Co</span><span>2</span></div>
</section>

<section class="slide" style="left:617px;top:94px">
  <div class="brand"><i></i>Valmin &amp; Co</div>
  <div class="photo" role="img" aria-label="Photo of a laptop with financial charts on a desk" style="left:18px;top:0;width:157px;height:210px;border-bottom-right-radius:40px"></div>
  <div class="abs" style="left:195px;top:42px;font-size:15px;color:var(--orange)">Your title slide here</div>
  <div class="abs h" style="left:195px;top:70px;width:210px;color:var(--ink);font-size:5.2px">What is Lorem Ipsum Lorem Ipsum is simply dummy text of the printing and typesetting industry</div>
  <div class="abs p" style="left:195px;top:92px">What is Lorem Ipsum?</div>
  <p class="abs p" style="left:195px;top:104px;width:210px">Lorem ipsum is simply dummy text of the printing and typesetting industry. Lorem Ipsum has been the industry's standard dummy text ever since the 1500s, when an unknown printer took a galley of type and scrambled it to make a type specimen book. It has survived not only five centuries, but also the leap into electronic typesetting, remaining essentially unchanged. It was popularised in the 1960s with the release of Linetype sheets containing Lorem Ipsum passages, and more recently with desktop publishing software like PageWright Studio including versions of Lorem Ipsum.</p>
  <p class="abs p" style="left:195px;top:178px;color:var(--orange)">Lorem ipsum is simply dummy text of the printing and typesetting industry.</p>
  <div class="foot"><span>Copyright © 2023 Valmin &amp; Co</span><span>3</span></div>
</section>

<section class="slide" style="left:910px;top:94px">
  <div class="abs" style="left:20px;top:18px;display:flex;gap:3px;align-items:center;font-size:5px;font-weight:600;color:var(--orange)"><i style="display:block;width:6px;height:6px;background:var(--orange)"></i>Valmin &amp; Co</div>
  <div class="photo warm" role="img" aria-label="Photo of a businesswoman using a tablet" style="left:252px;top:0;width:157px;height:210px;border-bottom-left-radius:40px;border-bottom-right-radius:20px"></div>
  <div class="abs" style="left:20px;top:38px;font-size:11px;color:var(--orange)">Your title slide here</div>
  <div class="abs h" style="left:20px;top:56px;width:215px;color:var(--ink);font-size:5.2px">What is Lorem Ipsum Lorem Ipsum is simply dummy text of the printing and typesetting industry. Lorem Ipsum has been the industry's standard dummy text ever since the 1500s,</div>
  <div class="abs p" style="left:20px;top:92px">What is Lorem Ipsum?</div>
  <p class="abs p" style="left:20px;top:104px;width:215px">Lorem Ipsum is simply dummy text of the printing and typesetting industry. Lorem Ipsum has been the industry's standard dummy text ever since the 1500s, when an unknown printer took a galley of type and scrambled it to make a type specimen book. It has survived not only five centuries, but also the leap into electronic typesetting, remaining essentially unchanged. It was popularised in the 1960s with the release of Linetype sheets containing Lorem Ipsum passages, and more recently with desktop publishing software like PageWright Studio including versions of Lorem Ipsum.</p>
  <div class="foot"><span>Copyright © 2023 Valmin &amp; Co</span><span>4</span></div>
</section>

<!-- Row 2 -->
<section class="slide" style="left:29px;top:310px">
  <div class="abs" style="left:20px;top:10px;display:flex;gap:3px;align-items:center;font-size:5px;font-weight:600;color:var(--orange)"><i style="display:block;width:6px;height:6px;background:var(--orange)"></i>Valmin &amp; Co</div>
  <div class="photo warm" role="img" aria-label="Photo of a person pointing at a printed report" style="left:252px;top:0;width:157px;height:212px;border-top-left-radius:40px"></div>
  <div class="abs" style="left:20px;top:44px;font-size:11px;color:var(--orange)">Your title slide here</div>
  <div class="abs h" style="left:20px;top:66px;color:var(--ink);font-size:6px">What is Lorem Ipsum Lorem Ipsum is simply</div>
  <div class="abs ho" style="left:20px;top:88px;font-size:4.8px;color:var(--brown)">What is Lorem Ipsum?</div>
  <p class="abs p" style="left:20px;top:100px;width:210px">Lorem Ipsum is simply dummy text of the printing and typesetting industry. Lorem Ipsum has been the industry's standard dummy text ever since the 1500s, when an unknown printer took a galley of type and scrambled it to make a type specimen book. It has survived not only five centuries, but also the leap into electronic typesetting, remaining essentially</p>
  <div class="abs ho" style="left:20px;top:152px;font-size:4.8px;color:var(--brown)">What is Lorem Ipsum?</div>
  <p class="abs p" style="left:20px;top:164px;width:210px">Lorem Ipsum is simply dummy text of the printing and typesetting industry. Lorem Ipsum has been the industry's standard dummy text ever since the 1500s, when an unknown printer took a galley of type and scrambled it to make a type specimen book. It has survived not only five centuries, but also the leap into electronic typesetting, remaining essentially</p>
  <div class="foot"><span>Copyright © 2023 Valmin &amp; Co</span><span>5</span></div>
</section>

<section class="slide" style="left:323px;top:307px">
  <div class="brand"><i></i>Valmin &amp; Co</div>
  <div class="ttl">Your title slide here</div>
  <div class="band">Lorem Ipsum is simply dummy text of the printing and typesetting industry. Lorem Ipsum has been the industry's standard dummy text ever since the 1500s, when an unknown printer took a galley of type and scrambled it to</div>
  <div class="circle photo" role="img" aria-label="Photo of colleagues shaking hands" style="left:66px;top:70px;width:54px;height:54px"></div>
  <div class="circle photo warm" role="img" aria-label="Photo of a team meeting at a table" style="left:186px;top:70px;width:54px;height:54px"></div>
  <div class="circle photo" role="img" aria-label="Photo of a person working on a laptop" style="left:306px;top:70px;width:54px;height:54px"></div>
  <div class="cols3" style="left:33px;right:33px;top:132px;text-align:center">
    <div><div class="ho" style="font-weight:400;font-size:6px">What is Lorem Ipsum?</div><div class="p" style="margin:8px 0 6px;color:#444">Simply Dummy Text</div><p class="p">Lorem Ipsum is simply dummy text of the printing and typesetting industry.</p></div>
    <div><div class="ho" style="font-weight:400;font-size:6px;color:var(--brown)">What is Lorem Ipsum?</div><div class="p" style="margin:8px 0 6px;color:#444">Simply Dummy Text</div><p class="p">Lorem Ipsum is simply dummy text of the printing and typesetting industry.</p></div>
    <div><div class="ho" style="font-weight:400;font-size:6px;color:var(--brown)">What is Lorem Ipsum?</div><div class="p" style="margin:8px 0 6px;color:#444">Simply Dummy Text</div><p class="p">Lorem Ipsum is simply dummy text of the printing and typesetting industry.</p></div>
  </div>
  <div class="foot"><span>Copyright © 2023 Valmin &amp; Co</span><span>6</span></div>
</section>

<section class="slide" style="left:617px;top:307px">
  <div class="brand"><i></i>Valmin &amp; Co</div>
  <div class="ttl">Your title slide here</div>
  <div class="band">Lorem Ipsum is simply dummy text of the printing and typesetting industry. Lorem Ipsum has been the industry's standard dummy text ever since the 1500s, when an unknown printer took a galley of type and scrambled it to</div>
  <div class="abs" style="left:12px;right:12px;top:82px;display:grid;grid-template-columns:repeat(5,1fr);gap:6px">
    <div><svg width="20" height="20" viewBox="0 0 20 20" style="display:block;margin:0 auto 10px"><g fill="none" stroke="#e0561f" stroke-width="1.5"><circle cx="10" cy="10" r="3"/><circle cx="3" cy="3" r="2"/><circle cx="17" cy="3" r="2"/><circle cx="3" cy="17" r="2"/><circle cx="17" cy="17" r="2"/><path d="M5 5l3 3M15 5l-3 3M5 15l3-3M15 15l-3-3"/></g></svg><div class="h" style="font-size:4.8px">What is Lorem Ipsum</div><p class="p" style="margin-top:8px">• Lorem Ipsum is simply dummy text of the printing<br><br>• typesetting industry. Lorem Ipsum has been</p></div>
    <div><svg width="20" height="20" viewBox="0 0 20 20" style="display:block;margin:0 auto 10px"><g fill="none" stroke="#e0561f" stroke-width="1.5"><rect x="7" y="2" width="11" height="4"/><rect x="7" y="8" width="11" height="4"/><rect x="7" y="14" width="11" height="4"/><path d="M3 2v14h4"/></g></svg><div class="h" style="font-size:4.8px">What is Lorem Ipsum</div><p class="p" style="margin-top:8px">• Lorem Ipsum is simply dummy text of the printing<br><br>• typesetting industry. Lorem Ipsum has been</p></div>
    <div><svg width="20" height="20" viewBox="0 0 20 20" style="display:block;margin:0 auto 10px"><g fill="none" stroke="#e0561f" stroke-width="1.5"><rect x="3" y="3" width="13" height="16"/><path d="M6 8h7M6 11h7M6 14h4M15 2l3 3-6 6h-3v-3z"/></g></svg><div class="h" style="font-size:4.8px">What is Lorem Ipsum</div><p class="p" style="margin-top:8px">• Lorem Ipsum is simply dummy text of the printing<br><br>• typesetting industry. Lorem Ipsum has been</p></div>
    <div><svg width="20" height="20" viewBox="0 0 20 20" style="display:block;margin:0 auto 10px"><g fill="#e0561f"><rect x="4" y="1" width="12" height="6"/><circle cx="5" cy="11" r="2"/><circle cx="10" cy="10" r="2.3"/><circle cx="15" cy="11" r="2"/><path d="M1 18c0-3 2-5 4-5s4 2 4 5zM6 18c0-3 2-5 4-5s4 2 4 5zM11 18c0-3 2-5 4-5s4 2 4 5z"/></g></svg><div class="h" style="font-size:4.8px">What is Lorem Ipsum</div><p class="p" style="margin-top:8px">• Lorem Ipsum is simply dummy text of the printing<br><br>• typesetting industry. Lorem Ipsum has been</p></div>
    <div><svg width="20" height="20" viewBox="0 0 20 20" style="display:block;margin:0 auto 10px"><path d="M1 18V9l4 3 4-5 4 4 6-2v9z" fill="#e0561f"/><circle cx="14" cy="5" r="4" fill="#e0561f"/><path d="M12 5l1.5 1.5L16 4" fill="none" stroke="#fff" stroke-width="1"/></svg><div class="h" style="font-size:4.8px">What is Lorem Ipsum</div><p class="p" style="margin-top:8px">• Lorem Ipsum is simply dummy text of the printing<br><br>• typesetting industry. Lorem Ipsum has been</p></div>
  </div>
  <div class="foot"><span>Copyright © 2023 Valmin &amp; Co</span><span>7</span></div>
</section>

<section class="slide" style="left:910px;top:310px">
  <div class="brand"><i></i>Valmin &amp; Co</div>
  <div class="ttl">Your title slide here</div>
  <div class="band">Lorem Ipsum is simply dummy text of the printing and typesetting industry.</div>
  <div class="abs" style="left:30px;right:20px;top:72px;display:grid;grid-template-columns:repeat(3,1fr);row-gap:16px;column-gap:8px">
    <div style="display:flex;gap:6px"><svg width="16" height="16" viewBox="0 0 16 16"><circle cx="8" cy="8" r="6" fill="none" stroke="#e0561f" stroke-width="2" stroke-dasharray="3 1.5"/></svg><div><div class="ho" style="font-size:4.8px">Your subtitle here</div><p class="p" style="font-size:3.8px;padding-left:6px">Lorem Ipsum is simply dummy text of the printing and Lorem</p></div></div>
    <div style="display:flex;gap:6px"><svg width="16" height="16" viewBox="0 0 16 16"><rect x="3" y="2" width="10" height="12" fill="none" stroke="#e0561f" stroke-width="1.4"/><path d="M5 6h6M5 9h6" stroke="#e0561f"/></svg><div><div class="ho" style="font-size:4.8px">Your subtitle here</div><p class="p" style="font-size:3.8px;padding-left:6px">Lorem Ipsum is simply dummy text of the printing and Lorem</p></div></div>
    <div style="display:flex;gap:6px"><svg width="16" height="16" viewBox="0 0 16 16"><path d="M2 6l4 4 4-4 4 4" fill="none" stroke="#7a2a12" stroke-width="2"/></svg><div><div class="ho" style="font-size:4.8px">Your subtitle here</div><p class="p" style="font-size:3.8px;padding-left:6px">Lorem Ipsum is simply dummy text of the printing and Lorem</p></div></div>
    <div style="display:flex;gap:6px"><svg width="16" height="16" viewBox="0 0 16 16"><circle cx="8" cy="8" r="5" fill="none" stroke="#7a2a12" stroke-width="2"/><circle cx="8" cy="8" r="2" fill="#e0561f"/></svg><div><div class="ho" style="font-size:4.8px">Your subtitle here</div><p class="p" style="font-size:3.8px;padding-left:6px">Lorem Ipsum is simply dummy text of the printing and Lorem</p></div></div>
    <div style="display:flex;gap:6px"><svg width="16" height="16" viewBox="0 0 16 16"><g fill="#7a2a12"><circle cx="5" cy="5" r="2"/><circle cx="11" cy="5" r="2"/><rect x="2" y="9" width="12" height="5"/></g></svg><div><div class="ho" style="font-size:4.8px">Your subtitle here</div><p class="p" style="font-size:3.8px;padding-left:6px">Lorem Ipsum is simply dummy text of the printing and Lorem</p></div></div>
    <div style="display:flex;gap:6px"><svg width="16" height="16" viewBox="0 0 16 16"><path d="M8 2v8M5 7l3 3 3-3M2 11v3h12v-3" fill="none" stroke="#e0561f" stroke-width="2"/></svg><div><div class="ho" style="font-size:4.8px">Your subtitle here</div><p class="p" style="font-size:3.8px;padding-left:6px">Lorem Ipsum is simply dummy text of the printing and Lorem</p></div></div>
    <div style="display:flex;gap:6px"><svg width="16" height="16" viewBox="0 0 16 16"><g stroke="#7a2a12" stroke-width="1.4"><path d="M8 2v12M2 8h12M4 4l8 8M12 4l-8 8"/></g></svg><div><div class="ho" style="font-size:4.8px">Your subtitle here</div><p class="p" style="font-size:3.8px;padding-left:6px">Lorem Ipsum is simply dummy text of the printing and Lorem</p></div></div>
    <div style="display:flex;gap:6px"><svg width="16" height="16" viewBox="0 0 16 16"><circle cx="8" cy="8" r="6" fill="#e0561f"/><circle cx="8" cy="8" r="2.5" fill="#fff"/></svg><div><div class="ho" style="font-size:4.8px">Your subtitle here</div><p class="p" style="font-size:3.8px;padding-left:6px">Lorem Ipsum is simply dummy text of the printing and Lorem</p></div></div>
    <div style="display:flex;gap:6px"><svg width="16" height="16" viewBox="0 0 16 16"><g fill="none" stroke="#e0561f" stroke-width="1.4"><rect x="2" y="2" width="4" height="4"/><rect x="10" y="10" width="4" height="4"/><path d="M6 4h6v6M4 6v6h6"/></g></svg><div><div class="ho" style="font-size:4.8px">Your subtitle here</div><p class="p" style="font-size:3.8px;padding-left:6px">Lorem Ipsum is simply dummy text of the printing and Lorem</p></div></div>
  </div>
  <div class="foot"><span>Copyright © 2023 Valmin &amp; Co</span><span>8</span></div>
</section>

<!-- Row 3 -->
<section class="slide" style="left:29px;top:527px">
  <div class="abs" style="left:0;right:0;top:0;height:80px;background:#c9c9c9"></div>
  <div class="brand" style="color:#fff"><i style="background:#fff"></i>Valmin &amp; Co</div>
  <div class="ttl" style="color:#fff;top:12px;font-size:11px;font-weight:300">Describe three concepts</div>
  <p class="abs p" style="left:10px;right:10px;top:28px;text-align:center;color:#f4f4f4">Lorem Ipsum is simply dummy text of the printing and typesetting industry. Lorem Ipsum has been the industry's standard dummy text ever since the 1500s, when an unknown printer took a galley of type and scrambled it to make a type specimen book. It has survived not only five centuries, but also the leap into electronic typesetting, remaining essentially</p>
  <div class="cols3" style="left:12px;right:12px;top:94px">
    <div><div style="font-size:7px;color:var(--brown);text-align:center;margin-bottom:10px">What is Lorem Ipsum?</div><p class="p" style="text-align:justify">Lorem Ipsum is simply dummy text of the printing and typesetting industry. Lorem Ipsum has been the industry's standard dummy text ever since the 1500s, when an unknown printer took a galley of type and scrambled it to make a type specimen book. It has survived not only five centuries, but also the leap into electronic typesetting, remaining essentially</p></div>
    <div><div style="font-size:7px;color:var(--brown);text-align:center;margin-bottom:10px">What is Lorem Ipsum?</div><p class="p" style="text-align:justify">Lorem Ipsum is simply dummy text of the printing and typesetting industry. Lorem Ipsum has been the industry's standard dummy text ever since the 1500s, when an unknown printer took a galley of type and scrambled it to make a type specimen book. It has survived not only five centuries, but also the leap into electronic typesetting, remaining essentially</p></div>
    <div><div style="font-size:7px;color:var(--brown);text-align:center;margin-bottom:10px">What is Lorem Ipsum?</div><p class="p" style="text-align:justify">Lorem Ipsum is simply dummy text of the printing and typesetting industry. Lorem Ipsum has been the industry's standard dummy text ever since the 1500s, when an unknown printer took a galley of type and scrambled it to make a type specimen book. It has survived not only five centuries, but also the leap into electronic typesetting, remaining essentially</p></div>
  </div>
</section>

<section class="slide" style="left:323px;top:522px">
  <div class="brand"><i></i>Valmin &amp; Co</div>
  <div class="ttl">Data Table Slide</div>
  <div class="band">Lorem Ipsum is simply dummy text of the printing and typesetting industry. Lorem Ipsum has been the industry's standard dummy text ever since the 1500s, when an unknown printer took a galley of type and scrambled it to make a type specimen book. It has survived not only five centuries, but also the leap into electronic typesetting, remaining essentially unchanged</div>
  <table class="data">
    <tr><th style="background:var(--orange)"></th><th>Data 2</th><th>Data 3</th><th>Data 4</th><th>Data 5</th><th>Data 6</th></tr>
    <tr><td>Title</td><td>12346</td><td>2356</td><td>5689</td><td>9874</td><td>63698</td></tr>
    <tr><td>Title</td><td>32456</td><td>45698</td><td>9875</td><td>96354</td><td>36548</td></tr>
    <tr><td>Title</td><td>12346</td><td>2356</td><td>5689</td><td>9874</td><td>63698</td></tr>
    <tr><td>Title</td><td>32456</td><td>45698</td><td>9875</td><td>96354</td><td>36548</td></tr>
  </table>
  <div class="foot"><span>Copyright © 2023 Valmin &amp; Co</span><span>10</span></div>
</section>

<section class="slide" style="left:617px;top:527px">
  <div class="brand"><i></i>Valmin &amp; Co</div>
  <div class="ttl">Your title slide here</div>
  <div class="band">Lorem Ipsum is simply dummy text of the printing and typesetting industry.</div>
  <div class="abs" style="left:30px;right:20px;top:72px;display:grid;grid-template-columns:repeat(3,1fr);row-gap:14px">
    <div style="display:flex;gap:10px;align-items:center"><span class="num">1</span><div><div class="ho" style="font-size:4.8px">Your subtitle here</div><p class="p" style="font-size:3.8px">Lorem Ipsum is simply dummy text of the printing and Lorem</p></div></div>
    <div style="display:flex;gap:10px;align-items:center"><span class="num" style="color:#555">4</span><div><div class="h" style="font-size:4.8px;color:#444;font-weight:500">Your subtitle here</div><p class="p" style="font-size:3.8px">Lorem Ipsum is simply dummy text of the printing and Lorem</p></div></div>
    <div style="display:flex;gap:10px;align-items:center"><span class="num">7</span><div><div class="ho" style="font-size:4.8px">Your subtitle here</div><p class="p" style="font-size:3.8px">Lorem Ipsum is simply dummy text of the printing and Lorem</p></div></div>
    <div style="display:flex;gap:10px;align-items:center"><span class="num dark">2</span><div><div class="ho" style="font-size:4.8px">Your subtitle here</div><p class="p" style="font-size:3.8px">Lorem Ipsum is simply dummy text of the printing and Lorem</p></div></div>
    <div style="display:flex;gap:10px;align-items:center"><span class="num" style="color:#555">5</span><div><div class="h" style="font-size:4.8px;color:#444;font-weight:500">Your subtitle here</div><p class="p" style="font-size:3.8px">Lorem Ipsum is simply dummy text of the printing and Lorem</p></div></div>
    <div style="display:flex;gap:10px;align-items:center"><span class="num dark">8</span><div><div class="h" style="font-size:4.8px">Your subtitle here</div><p class="p" style="font-size:3.8px">Lorem Ipsum is simply dummy text of the printing and Lorem</p></div></div>
    <div style="display:flex;gap:10px;align-items:center"><span class="num dark">3</span><div><div class="h" style="font-size:4.8px">Your subtitle here</div><p class="p" style="font-size:3.8px">Lorem Ipsum is simply dummy text of the printing and Lorem</p></div></div>
    <div style="display:flex;gap:10px;align-items:center"><span class="num" style="color:#555">6</span><div><div class="h" style="font-size:4.8px;color:#444;font-weight:500">Your subtitle here</div><p class="p" style="font-size:3.8px">Lorem Ipsum is simply dummy text of the printing and Lorem</p></div></div>
    <div style="display:flex;gap:10px;align-items:center"><span class="num">9</span><div><div class="ho" style="font-size:4.8px">Your subtitle here</div><p class="p" style="font-size:3.8px">Lorem Ipsum is simply dummy text of the printing and Lorem</p></div></div>
  </div>
  <div class="foot"><span>Copyright © 2023 Valmin &amp; Co</span><span>11</span></div>
</section>

<section class="slide" style="left:910px;top:527px">
  <div class="brand"><i></i>Valmin &amp; Co</div>
  <div class="ttl">Nine themes title slide</div>
  <div class="rule"></div>
  <div class="abs" style="left:20px;right:20px;top:54px;display:grid;grid-template-columns:repeat(3,1fr);column-gap:12px;row-gap:12px">
    <div><div class="h" style="font-size:4.8px">What is Lorem Ipsum?</div><p class="p" style="font-size:3.8px;text-align:justify">Lorem Ipsum is simply dummy text of the printing and typesetting industry. Lorem Ipsum has been the industry's standard dummy text ever since the 1500s, when an unknown printer took a galley of type and scrambled it to make a type specimen book.</p></div>
    <div><div class="h" style="font-size:4.8px">What is Lorem Ipsum?</div><p class="p" style="font-size:3.8px;text-align:justify">Lorem Ipsum is simply dummy text of the printing and typesetting industry. Lorem Ipsum has been the industry's standard dummy text ever since the 1500s, when an unknown printer took a galley of type and scrambled it to make a type specimen book.</p></div>
    <div><div class="h" style="font-size:4.8px">What is Lorem Ipsum?</div><p class="p" style="font-size:3.8px;text-align:justify">Lorem Ipsum is simply dummy text of the printing and typesetting industry. Lorem Ipsum has been the industry's standard dummy text ever since the 1500s, when an unknown printer took a galley of type and scrambled it to make a type specimen book.</p></div>
    <div><div class="h" style="font-size:4.8px">What is Lorem Ipsum?</div><p class="p" style="font-size:3.8px;text-align:justify">Lorem Ipsum is simply dummy text of the printing and typesetting industry. Lorem Ipsum has been the industry's standard dummy text ever since the 1500s, when an unknown printer took a galley of type and scrambled it to make a type specimen book.</p></div>
    <div><div class="h" style="font-size:4.8px">What is Lorem Ipsum?</div><p class="p" style="font-size:3.8px;text-align:justify">Lorem Ipsum is simply dummy text of the printing and typesetting industry. Lorem Ipsum has been the industry's standard dummy text ever since the 1500s, when an unknown printer took a galley of type and scrambled it to make a type specimen book.</p></div>
    <div><div class="h" style="font-size:4.8px">What is Lorem Ipsum?</div><p class="p" style="font-size:3.8px;text-align:justify">Lorem Ipsum is simply dummy text of the printing and typesetting industry. Lorem Ipsum has been the industry's standard dummy text ever since the 1500s, when an unknown printer took a galley of type and scrambled it to make a type specimen book.</p></div>
    <div><div class="h" style="font-size:4.8px">What is Lorem Ipsum?</div><p class="p" style="font-size:3.8px;text-align:justify">Lorem Ipsum is simply dummy text of the printing and typesetting industry. Lorem Ipsum has been the industry's standard dummy text ever since the 1500s, when an unknown printer took a galley of type and scrambled it to make a type specimen book.</p></div>
    <div><div class="h" style="font-size:4.8px">What is Lorem Ipsum?</div><p class="p" style="font-size:3.8px;text-align:justify">Lorem Ipsum is simply dummy text of the printing and typesetting industry. Lorem Ipsum has been the industry's standard dummy text ever since the 1500s, when an unknown printer took a galley of type and scrambled it to make a type specimen book.</p></div>
    <div><div class="h" style="font-size:4.8px">What is Lorem Ipsum?</div><p class="p" style="font-size:3.8px;text-align:justify">Lorem Ipsum is simply dummy text of the printing and typesetting industry. Lorem Ipsum has been the industry's standard dummy text ever since the 1500s, when an unknown printer took a galley of type and scrambled it to make a type specimen book.</p></div>
  </div>
  <div class="foot"><span>Copyright © 2023 Valmin &amp; Co</span><span>12</span></div>
</section>

<!-- Row 4 -->
<section class="slide" style="left:29px;top:743px">
  <div class="brand"><i></i>Valmin &amp; Co</div>
  <div class="ttl">Your title slide here</div>
  <div class="band">Lorem Ipsum is simply dummy text of the printing and typesetting industry.</div>
  <div class="abs" style="left:58px;right:40px;top:78px;display:grid;grid-template-columns:1fr 1fr;row-gap:20px">
    <div style="display:flex;gap:12px;align-items:center"><span class="num">1</span><div><div class="ho" style="font-size:4.8px">Your subtitle here</div><p class="p" style="font-size:3.8px">Lorem Ipsum is simply dummy text of the printing and typesetting industry. Lorem</p></div></div>
    <div style="display:flex;gap:12px;align-items:center"><span class="num">2</span><div><div class="ho" style="font-size:4.8px">Your subtitle here</div><p class="p" style="font-size:3.8px">Lorem Ipsum is simply dummy text of the printing and typesetting industry. Lorem</p></div></div>
    <div style="display:flex;gap:12px;align-items:center"><span class="num dark">3</span><div><div class="h" style="font-size:4.8px">Your subtitle here</div><p class="p" style="font-size:3.8px">Lorem Ipsum is simply dummy text of the printing and typesetting industry. Lorem</p></div></div>
    <div style="display:flex;gap:12px;align-items:center"><span class="num" style="color:#555">4</span><div><div class="h" style="font-size:4.8px;color:#555;font-weight:500">Your subtitle here</div><p class="p" style="font-size:3.8px">Lorem Ipsum is simply dummy text of the printing and typesetting industry. Lorem</p></div></div>
    <div style="display:flex;gap:12px;align-items:center"><span class="num dark">5</span><div><div class="h" style="font-size:4.8px">Your subtitle here</div><p class="p" style="font-size:3.8px">Lorem Ipsum is simply dummy text of the printing and typesetting industry. Lorem</p></div></div>
    <div style="display:flex;gap:12px;align-items:center"><span class="num" style="color:#555">6</span><div><div class="h" style="font-size:4.8px;color:#555;font-weight:500">Your subtitle here</div><p class="p" style="font-size:3.8px">Lorem Ipsum is simply dummy text of the printing and typesetting industry. Lorem</p></div></div>
  </div>
  <div class="foot"><span>Copyright © 2023 Valmin &amp; Co</span><span>13</span></div>
</section>

<section class="slide" style="left:323px;top:743px">
  <div class="brand"><i></i>Valmin &amp; Co</div>
  <div class="ttl">Your title slide here</div>
  <div class="band">Lorem Ipsum is simply dummy text of the printing and typesetting industry.</div>
  <div class="abs" style="left:35px;right:30px;top:82px;display:grid;grid-template-columns:repeat(3,1fr);row-gap:24px">
    <div style="display:flex;gap:12px;align-items:center"><span class="num dark">1</span><span class="h" style="font-size:4.8px">Your subtitle here</span></div>
    <div style="display:flex;gap:12px;align-items:center"><span class="num">4</span><span class="h" style="font-size:4.8px">Your subtitle here</span></div>
    <div style="display:flex;gap:12px;align-items:center"><span class="num" style="color:var(--orange-soft)">7</span><span class="h" style="font-size:4.8px">Your subtitle here</span></div>
    <div style="display:flex;gap:12px;align-items:center"><span class="num dark">2</span><span class="h" style="font-size:4.8px">Your subtitle here</span></div>
    <div style="display:flex;gap:12px;align-items:center"><span class="num" style="color:#555">5</span><span class="h" style="font-size:4.8px">Your subtitle here</span></div>
    <div style="display:flex;gap:12px;align-items:center"><span class="num dark">8</span><span class="h" style="font-size:4.8px">Your subtitle here</span></div>
    <div style="display:flex;gap:12px;align-items:center"><span class="num dark">3</span><span class="h" style="font-size:4.8px">Your subtitle here</span></div>
    <div style="display:flex;gap:12px;align-items:center"><span class="num" style="color:#555">6</span><span class="h" style="font-size:4.8px">Your subtitle here</span></div>
    <div style="display:flex;gap:12px;align-items:center"><span class="num dark">9</span><span class="h" style="font-size:4.8px">Your subtitle here</span></div>
  </div>
  <div class="foot"><span>Copyright © 2023 Valmin &amp; Co</span><span>14</span></div>
</section>

<section class="slide" style="left:617px;top:743px">
  <div class="brand"><i></i>Valmin &amp; Co</div>
  <div class="ttl">Solo Text Slide</div>
  <div class="rule"></div>
  <div class="abs" style="left:20px;right:25px;top:64px">
    <div class="h" style="font-size:5px">What is Lorem Ipsum?</div>
    <p class="p" style="margin-bottom:12px">Lorem Ipsum is simply dummy text of the printing and typesetting industry. Lorem Ipsum has been the industry's standard dummy text ever since the 1500s, when an unknown printer took a galley of type and scrambled it to make a type specimen book. It has survived not only five centuries, but also the leap into electronic typesetting, remaining essentially unchanged. It was popularised in the 1960s with the release of Linetype sheets containing Lorem Ipsum passages, and more recently with desktop publishing software like PageWright Studio including versions of Lorem Ipsum.</p>
    <div class="h" style="font-size:5px">Why do we use it?</div>
    <p class="p">It is a long established fact that a reader will be distracted by the readable content of a page when looking at its layout. The point of using Lorem Ipsum is that it has a more-or-less normal distribution of letters, as opposed to using 'Content here, content here', making it look like readable English. Many desktop publishing packages and web page editors now use Lorem Ipsum as their default model text, and a search for 'lorem ipsum' will uncover many web sites still in their infancy. Various versions have evolved over the years, sometimes by accident, sometimes on purpose (injected humour and the like).</p>
  </div>
  <div class="foot"><span>Copyright © 2023 Valmin &amp; Co</span><span>16</span></div>
</section>

<section class="slide" style="left:910px;top:743px">
  <div class="brand"><i></i>Valmin &amp; Co</div>
  <div class="ttl">Data Chart Slide</div>
  <div class="band">Lorem Ipsum is simply dummy text of the printing and typesetting industry. Lorem Ipsum has been the industry's standard dummy text ever since the 1500s, when an unknown printer took a galley of type and scrambled it to make a type specimen book. It has survived not only five centuries, but also the leap into electronic typesetting, remaining essentially unchanged</div>
  <div class="abs" style="left:20px;top:80px;width:150px;display:grid;row-gap:8px">
    <div style="display:flex;gap:10px;align-items:center"><span class="num dark">1</span><p class="p" style="font-size:3.6px;color:var(--orange)">Lorem ipsum is simply dummy text of the printing and typesetting industry. Lorem Ipsum has been the industry's standard dummy text ever since the 1500s, when an unknown printer took a galley of type and scrambled it to make a type specimen</p></div>
    <div style="display:flex;gap:10px;align-items:center"><span class="num dark">2</span><p class="p" style="font-size:3.6px;color:var(--orange)">Lorem ipsum is simply dummy text of the printing and typesetting industry. Lorem Ipsum has been the industry's standard dummy text ever since the 1500s, when an unknown printer took a galley of type and scrambled it to make a type specimen</p></div>
    <div style="display:flex;gap:10px;align-items:center"><span class="num dark">3</span><p class="p" style="font-size:3.6px;color:var(--orange)">Lorem ipsum is simply dummy text of the printing and typesetting industry. Lorem Ipsum has been the industry's standard dummy text ever since the 1500s, when an unknown printer took a galley of type and scrambled it to make a type specimen</p></div>
  </div>
  <svg class="abs" style="left:198px;top:80px" width="210" height="120" viewBox="0 0 210 120" font-family="Montserrat,sans-serif">
    <text x="110" y="8" font-size="6" fill="#3a8fb7" text-anchor="middle">Chart Title</text>
    <g font-size="3.5" fill="#e0561f"><text x="2" y="22">6</text><text x="2" y="35">5</text><text x="2" y="48">4</text><text x="2" y="61">3</text><text x="2" y="74">2</text><text x="2" y="87">1</text><text x="2" y="100">0</text></g>
    <g>
      <rect x="20" y="47" width="6" height="53" fill="#e0561f"/><rect x="27" y="68" width="6" height="32" fill="#8b2e12"/><rect x="34" y="75" width="6" height="25" fill="#5a1a08"/>
      <rect x="65" y="75" width="6" height="25" fill="#e0561f"/><rect x="72" y="45" width="6" height="55" fill="#8b2e12"/><rect x="79" y="76" width="6" height="24" fill="#5a1a08"/>
      <rect x="110" y="53" width="6" height="47" fill="#e0561f"/><rect x="117" y="79" width="6" height="21" fill="#8b2e12"/><rect x="124" y="62" width="6" height="38" fill="#5a1a08"/>
      <rect x="155" y="45" width="6" height="55" fill="#e0561f"/><rect x="162" y="58" width="6" height="42" fill="#8b2e12"/><rect x="169" y="36" width="6" height="64" fill="#5a1a08"/>
    </g>
    <g font-size="3.5" fill="#e0561f" text-anchor="middle"><text x="30" y="107">Category 1</text><text x="75" y="107">Category 2</text><text x="120" y="107">Category 3</text><text x="165" y="107">Category 4</text></g>
    <g font-size="3.5" fill="#7a2a12"><rect x="55" y="111" width="3" height="3" fill="#e0561f"/><text x="59" y="114">Series 1</text><rect x="80" y="111" width="3" height="3" fill="#8b2e12"/><text x="84" y="114">Series 2</text><rect x="105" y="111" width="3" height="3" fill="#5a1a08"/><text x="109" y="114">Series 3</text></g>
  </svg>
  <div class="foot"><span>Copyright © 2023 Valmin &amp; Co</span><span>17</span></div>
</section>

<!-- Row 5 -->
<section class="slide" style="left:29px;top:958px">
  <div class="brand"><i></i>Valmin &amp; Co</div>
  <div class="ttl">Data chart infographic slide</div>
  <div class="band">Lorem Ipsum is simply dummy text of the printing and typesetting industry.</div>
  <div class="abs" style="left:20px;width:90px;top:66px;text-align:center">
    <div style="font-size:10px;color:var(--orange)">DATA #</div><div class="ho" style="font-size:6px;margin:3px 0 5px">Subtitle Here</div><p class="p" style="font-size:3.6px;color:var(--orange)">Lorem Ipsum is simply dummy text of the printing and typesetting industry. Lorem Ipsum has</p>
    <div style="font-size:10px;color:var(--ink);margin-top:18px">DATA #</div><div class="h" style="font-size:6px;margin:3px 0 5px">Subtitle Here</div><p class="p" style="font-size:3.6px">Lorem Ipsum is simply dummy text of the printing and typesetting industry. Lorem Ipsum has</p>
  </div>
  <div class="abs" style="left:317px;width:90px;top:66px;text-align:center">
    <div style="font-size:10px;color:var(--orange)">DATA #</div><div class="ho" style="font-size:6px;margin:3px 0 5px">Subtitle Here</div><p class="p" style="font-size:3.6px">Lorem Ipsum is simply dummy text of the printing and typesetting industry. Lorem Ipsum has</p>
    <div style="font-size:10px;color:var(--orange);margin-top:18px">DATA #</div><div class="ho" style="font-size:6px;margin:3px 0 5px">Subtitle Here</div><p class="p" style="font-size:3.6px">Lorem Ipsum is simply dummy text of the printing and typesetting industry. Lorem Ipsum has</p>
  </div>
  <svg class="abs" style="left:122px;top:60px" width="180" height="150" viewBox="0 0 180 150" font-family="Montserrat,sans-serif">
    <text x="90" y="8" font-size="6" fill="#555" text-anchor="middle">Chart Title</text>
    <g font-size="3.5" fill="#555"><text x="2" y="20">5</text><text x="2" y="32">4.5</text><text x="2" y="44">4</text><text x="2" y="56">3.5</text><text x="2" y="68">3</text><text x="2" y="80">2.5</text><text x="2" y="92">2</text><text x="2" y="104">1.5</text><text x="2" y="116">1</text><text x="2" y="128">0.5</text></g>
    <line x1="14" y1="130" x2="175" y2="130" stroke="#ccc" stroke-width=".5"/>
    <g>
      <rect x="20" y="70" width="7" height="60" fill="#e0561f"/><rect x="28" y="100" width="7" height="30" fill="#f08a4b"/><rect x="36" y="60" width="7" height="70" fill="#d0481a"/><rect x="44" y="90" width="7" height="40" fill="#8b2e12"/>
      <rect x="60" y="30" width="7" height="100" fill="#e0561f"/><rect x="68" y="22" width="7" height="108" fill="#f08a4b"/><rect x="76" y="92" width="7" height="38" fill="#d0481a"/><rect x="84" y="75" width="7" height="55" fill="#8b2e12"/>
      <rect x="100" y="60" width="7" height="70" fill="#e0561f"/><rect x="108" y="44" width="7" height="86" fill="#f08a4b"/><rect x="116" y="26" width="7" height="104" fill="#d0481a"/><rect x="124" y="70" width="7" height="60" fill="#8b2e12"/>
      <rect x="140" y="36" width="7" height="94" fill="#e0561f"/><rect x="148" y="44" width="7" height="86" fill="#f08a4b"/><rect x="156" y="20" width="7" height="110" fill="#d0481a"/><rect x="164" y="90" width="7" height="40" fill="#8b2e12"/>
    </g>
    <g font-size="3.5" fill="#555" text-anchor="middle"><text x="36" y="137">Category 1</text><text x="76" y="137">Category 2</text><text x="116" y="137">Category 3</text><text x="156" y="137">Category 4</text></g>
    <g font-size="3.5" fill="#555"><rect x="30" y="142" width="3" height="3" fill="#e0561f"/><text x="34" y="145">Series 1</text><rect x="60" y="142" width="3" height="3" fill="#f08a4b"/><text x="64" y="145">Series 2</text><rect x="90" y="142" width="3" height="3" fill="#d0481a"/><text x="94" y="145">Series 3</text><rect x="120" y="142" width="3" height="3" fill="#8b2e12"/><text x="124" y="145">Series 4</text></g>
  </svg>
  <div class="foot"><span>Copyright © 2023 Valmin &amp; Co</span><span>18</span></div>
</section>

<section class="slide" style="left:323px;top:958px">
  <div class="brand"><i></i>Valmin &amp; Co</div>
  <div class="ttl">Your title slide here</div>
  <div class="rule"></div>
  <p class="abs p" style="left:30px;right:30px;top:46px;text-align:center">Lorem Ipsum is simply dummy text of the printing and typesetting industry. Lorem Ipsum has been the industry's standard dummy text ever since the 1500s, when an unknown printer took a galley of type and scrambled it to</p>
  <div class="abs" style="left:0;right:0;top:113px;height:1px;background:#e6c4b6"></div>
  <div class="circle" style="left:36px;top:70px;width:78px;height:78px;border:3px solid var(--orange);border-bottom-color:transparent;border-right-color:transparent;transform:rotate(-20deg)"></div>
  <div class="circle" style="left:176px;top:70px;width:78px;height:78px;border:3px solid var(--orange);border-bottom-color:transparent;border-right-color:transparent;transform:rotate(-20deg)"></div>
  <div class="circle" style="left:316px;top:70px;width:78px;height:78px;border:3px solid var(--orange);border-bottom-color:transparent;border-right-color:transparent;transform:rotate(-20deg)"></div>
  <div class="circle" style="left:106px;top:120px;width:78px;height:78px;border:3px solid var(--brown);border-top-color:transparent;border-left-color:transparent;transform:rotate(-20deg)"></div>
  <div class="circle" style="left:246px;top:120px;width:78px;height:78px;border:3px solid var(--brown);border-top-color:transparent;border-left-color:transparent;transform:rotate(-20deg)"></div>
  <div class="circle photo" role="img" aria-label="Photo of a handshake over a desk" style="left:42px;top:76px;width:66px;height:66px"></div>
  <div class="circle photo warm" role="img" aria-label="Photo of a laptop and notebook" style="left:182px;top:76px;width:66px;height:66px"></div>
  <div class="circle photo" role="img" aria-label="Photo of a person typing on a laptop" style="left:322px;top:76px;width:66px;height:66px"></div>
  <div class="circle photo warm" role="img" aria-label="Photo of colleagues reviewing papers" style="left:112px;top:126px;width:66px;height:66px"></div>
  <div class="circle photo" role="img" aria-label="Photo of hands writing notes" style="left:252px;top:126px;width:66px;height:66px"></div>
  <div class="abs" style="left:115px;width:60px;top:82px;text-align:center"><p class="p" style="font-size:3.8px;color:var(--brown);font-weight:600">Lorem Ipsum is simply dummy text of the</p><div class="ho" style="font-size:4.8px;color:var(--brown);margin-top:6px">Subtitle Here</div></div>
  <div class="abs" style="left:255px;width:60px;top:82px;text-align:center"><p class="p" style="font-size:3.8px;color:var(--brown);font-weight:600">Lorem Ipsum is simply dummy text of the</p><div class="ho" style="font-size:4.8px;color:var(--brown);margin-top:6px">Subtitle Here</div></div>
  <div class="abs" style="left:45px;width:60px;top:148px;text-align:center"><div class="ho" style="font-size:4.8px">Subtitle Here</div><p class="p" style="font-size:3.8px;color:var(--brown);font-weight:600;margin-top:6px">Lorem Ipsum is simply dummy text of the</p></div>
  <div class="abs" style="left:185px;width:60px;top:148px;text-align:center"><div class="ho" style="font-size:4.8px">Subtitle Here</div><p class="p" style="font-size:3.8px;color:var(--brown);font-weight:600;margin-top:6px">Lorem Ipsum is simply dummy text of the</p></div>
  <div class="abs" style="left:325px;width:60px;top:148px;text-align:center"><div class="ho" style="font-size:4.8px">Subtitle Here</div><p class="p" style="font-size:3.8px;color:var(--brown);font-weight:600;margin-top:6px">Lorem Ipsum is simply dummy text of the</p></div>
  <div class="foot"><span>Copyright © 2023 Valmin &amp; Co</span><span>19</span></div>
</section>

<section class="slide" style="left:617px;top:958px">
  <div class="brand"><i></i>Valmin &amp; Co</div>
  <div class="ttl">Your title slide here</div>
  <div class="rule"></div>
  <svg class="abs" style="left:0;top:0" width="427" height="240" viewBox="0 0 427 240">
    <polygon points="213,70 196,95 230,95" fill="#e0561f"/>
    <polygon points="194,98 232,98 226,106 200,106" fill="#f3e3d7"/>
    <polygon points="198,109 228,109 245,130 181,130" fill="#8b2e12"/>
    <polygon points="179,133 247,133 268,158 158,158" fill="#5a5a5a"/>
    <polygon points="213,158 268,158 247,133 213,150" fill="#444"/>
    <g stroke="#999" stroke-width=".6" fill="none"><path d="M245 110L272 86M150 117L200 117M255 140L276 159"/></g>
    <circle cx="278" cy="84" r="6" fill="#e0561f"/>
    <circle cx="142" cy="117" r="6" fill="#8b2e12"/>
    <circle cx="278" cy="160" r="6" fill="#5a1a08"/>
  </svg>
  <div class="abs" style="left:300px;top:64px;width:100px"><div class="ho" style="font-size:5.5px">Simply Dummy Text</div><p class="p" style="margin-top:4px">Lorem Ipsum is simply dummy text of the printing and typesetting industry. Lorem Ipsum has been</p></div>
  <div class="abs" style="left:50px;top:100px;width:85px;text-align:center"><div class="h" style="font-size:5.5px;color:var(--ink)">Simply Dummy Text</div><p class="p" style="margin-top:4px">Lorem Ipsum is simply dummy text of the printing and typesetting industry. Lorem Ipsum has been</p></div>
  <div class="abs" style="left:300px;top:150px;width:100px"><div class="h" style="font-size:5.5px;color:var(--ink)">Simply Dummy Text</div><p class="p" style="margin-top:4px">Lorem Ipsum is simply dummy text of the printing and typesetting industry. Lorem Ipsum has been</p></div>
  <div class="foot"><span>Copyright © 2023 Valmin &amp; Co</span><span>20</span></div>
</section>

<section class="slide" style="left:910px;top:958px">
  <div class="brand"><i></i>Valmin &amp; Co</div>
  <div class="ttl">Infographic slide</div>
  <div class="rule"></div>
  <svg class="abs" style="left:0;top:0" width="427" height="240" viewBox="0 0 427 240">
    <g stroke="#fff" stroke-width="2">
      <path d="M213 52C200 80 150 110 150 148L213 148Z" fill="#e0561f"/>
      <path d="M213 52C226 80 276 110 276 148L213 148Z" fill="#7a2a12"/>
      <path d="M150 148C150 185 182 210 213 210L213 148Z" fill="#f0832f"/>
      <path d="M276 148C276 185 244 210 213 210L213 148Z" fill="#5a1a08"/>
    </g>
    <g fill="none" stroke="#fff" stroke-width="1">
      <circle cx="188" cy="130" r="6"/><circle cx="238" cy="130" r="6"/>
      <circle cx="188" cy="170" r="5"/><path d="M188 160v-3M188 180v3M178 170h-3M198 170h3"/>
      <circle cx="238" cy="168" r="5"/><path d="M236 175h4M236 178h4"/>
    </g>
  </svg>
  <div class="abs" style="left:40px;width:80px;top:56px;text-align:center"><div style="font-size:9px;color:var(--orange)">Title 1</div><div class="ho" style="font-size:6px;margin:5px 0">Subtitle Here</div><p class="p">Lorem Ipsum is simply dummy text of the</p></div>
  <div class="abs" style="left:40px;width:80px;top:132px;text-align:center"><div style="font-size:9px;color:var(--orange-soft)">Title 1</div><div class="ho" style="font-size:6px;margin:5px 0;color:var(--orange-soft)">Subtitle Here</div><p class="p">Lorem Ipsum is simply dummy text of the</p></div>
  <div class="abs" style="left:305px;width:80px;top:56px;text-align:center"><div style="font-size:9px;color:var(--brown)">Title 1</div><div class="h" style="font-size:6px;margin:5px 0">Subtitle Here</div><p class="p">Lorem Ipsum is simply dummy text of the</p></div>
  <div class="abs" style="left:305px;width:80px;top:132px;text-align:center"><div style="font-size:9px;color:var(--brown-dark)">Title 1</div><div class="h" style="font-size:6px;margin:5px 0;color:var(--brown-dark)">Subtitle Here</div><p class="p">Lorem Ipsum is simply dummy text of the</p></div>
  <div class="foot"><span>Copyright © 2023 Valmin &amp; Co</span><span>21</span></div>
</section>

</main>
</body>
</html>
```